Bright Pathway! A website showcasing who I am as a person

Bright Pathway started out as idea for me to better myself as a person and work on small projects that would help me grow as a person. Now I want to build a website showcasing "Bright Pathway." I want the website to showcase who I am and how I have grown both professionally and personally. I can build the raw code of the website on my own but I am not really much of a designer. I am looking for a design where I can write and post blogs, articles and share my thoughts. A little about myself and the ideas and interests that I want to share
What is Bright Pathway
Who I am
Background - Professional
Brand Marketing
Email Automation
Hiking
Rock Climbing
Traveling
Exercising and Transformation
"Personal Thoughts"
Hopefully this is enough information to get people started on some designs.
Work
3 page

```html
<!DOCTYPE html>
<html lang="en">
<head>
<meta charset="utf-8">
<title>Bright Pathway — Blog</title>
<link href="https://fonts.googleapis.com/css2?family=Roboto:wght@400;500;700&family=Playfair+Display:wght@400;700&display=swap" rel="stylesheet">
<style>
:root{
  --orange:#f26522;
  --teal:#2e8c8a;
  --ink:#222222;
  --text:#555555;
  --muted:#8a8a8a;
  --line:#e2e2e2;
  --panel:#f2f2f2;
  --footer:#3b3b3b;
  --white:#ffffff;
}
*{box-sizing:border-box;margin:0;padding:0}
html,body{width:1200px;height:3076px;overflow:hidden;background:var(--white);font-family:"Roboto",Arial,sans-serif;color:var(--text)}
.page{position:relative;width:1200px;height:3076px}

/* Hero */
.hero{position:absolute;left:0;top:0;width:1200px;height:550px;overflow:hidden}
.hero-photo{position:absolute;inset:0;background:linear-gradient(90deg,#f4f5f6 0%,#eceff1 35%,#d9dee2 60%,#c9d0d5 80%,#e3e6e8 100%)}
.logo{position:absolute;left:108px;top:34px;font-weight:700;font-size:17px;color:var(--ink);letter-spacing:.5px}
.top-social{position:absolute;left:915px;top:18px;display:flex;gap:6px}
.dot{width:28px;height:28px;border-radius:50%;background:var(--teal)}
.dot.o{background:var(--orange)}
.hi-bubble{position:absolute;left:108px;top:78px}
.hi-bubble span{position:absolute;left:0;top:0;width:76px;height:76px;display:flex;align-items:center;justify-content:center;font-family:"Playfair Display",Georgia,serif;color:var(--white);font-size:38px}
.hero-name{position:absolute;left:108px;top:252px;font-family:"Playfair Display",Georgia,serif;font-size:66px;color:var(--teal);font-weight:400;line-height:1}
.hero-role{position:absolute;left:112px;top:330px;font-family:"Playfair Display",Georgia,serif;font-size:34px;color:var(--ink);line-height:1}

/* Posts */
.post{position:absolute;left:108px;width:644px;height:540px;border-bottom:1px solid var(--line)}
.meta{display:flex;gap:18px;font-size:11px;color:var(--muted);height:16px;align-items:center}
.meta b{color:var(--orange);font-weight:500}
.meta i{display:inline-block;width:9px;height:9px;background:var(--muted);margin-right:5px;vertical-align:-1px;border-radius:1px}
.post-title{margin-top:10px;font-size:19px;line-height:25px;font-weight:700;color:var(--ink);width:600px}
.post-image{margin-top:12px;width:644px;height:300px}
.excerpt{margin-top:20px;font-size:11px;line-height:16px;color:var(--text)}
.continue{display:block;text-align:center;margin-top:20px;font-size:10px;font-weight:700;letter-spacing:.5px;color:var(--ink)}

/* Sidebar */
.widget{position:absolute;left:772px;width:316px;background:var(--panel);padding:14px 14px}
.widget h3{font-family:"Playfair Display",Georgia,serif;font-size:17px;color:var(--ink);font-weight:700;padding-bottom:8px;position:relative}
.widget h3::after{content:"";position:absolute;left:0;right:0;bottom:0;height:4px;background:var(--orange)}
.widget h3.teal::after{background:var(--teal)}
.widget h3.dark::after{background:#555}
.about p{margin-top:12px;font-size:11px;line-height:16px}
.recent li{list-style:none;margin-top:14px}
.recent strong{display:block;font-size:13px;line-height:17px;color:var(--ink);font-weight:700}
.recent small{font-size:10px;color:var(--muted)}
.recent small b{color:var(--orange);font-weight:500}
.subscribe{background:var(--teal);padding:18px 30px}
.subscribe h3{color:var(--white)}
.subscribe h3::after{background:var(--white)}
.subscribe .field{margin-top:18px;height:30px;background:var(--white);border-radius:3px;font-size:10px;color:var(--muted);padding:9px 12px}
.subscribe .btn{margin-top:10px;height:30px;background:var(--orange);border-radius:3px;color:var(--white);font-size:10px;font-weight:700;text-align:center;line-height:30px;letter-spacing:.5px}
.archives ul{margin-top:14px;padding-left:16px}
.archives li{font-size:11px;line-height:20px;color:var(--text)}
.side-social{display:flex;gap:6px;margin-top:14px}

/* Pagination */
.pager{position:absolute;left:108px;top:2884px;width:644px;display:flex;justify-content:center;gap:8px}
.pager span{height:30px;min-width:30px;border:1px solid var(--line);border-radius:15px;font-size:10px;display:flex;align-items:center;justify-content:center;padding:0 10px;color:var(--text)}
.pager span.current{border-color:var(--orange);color:var(--orange)}

/* Footer */
.footer{position:absolute;left:0;top:2980px;width:1200px;height:96px;background:var(--footer);text-align:center;color:#bdbdbd}
.footer nav{padding-top:30px;font-size:11px;display:flex;justify-content:center;gap:14px}
.footer small{display:block;margin-top:10px;font-size:10px;color:#999}
.to-top{position:absolute;left:1052px;top:28px;width:32px;height:32px;background:#666;border-radius:3px}
</style>
</head>
<body>
<div class="page">

<header class="hero">
  <div class="hero-photo" role="img" aria-label="Portrait of a smiling businessman in a white shirt working at a laptop in a bright office"></div>
  <div class="logo">LOGO HERE</div>
  <div class="top-social"><div class="dot"></div><div class="dot"></div><div class="dot o"></div><div class="dot o"></div><div class="dot"></div></div>
  <div class="hi-bubble">
    <svg width="80" height="90" viewBox="0 0 80 90"><circle cx="38" cy="38" r="38" fill="#f26522"/><path d="M20 68 L14 88 L38 72 Z" fill="#f26522"/></svg>
    <span>Hi.</span>
  </div>
  <h1 class="hero-name">I'm Daniel</h1>
  <p class="hero-role">Professional Businessman</p>
</header>

<article class="post" style="top:600px">
  <div class="meta"><span><i></i>By <b>Daniel Reyes</b></span><span><i></i>28 March 2017</span><span><i></i>Brand Marketing</span></div>
  <h2 class="post-title">The standard Lorem Ipsum passage used since the awesome as well as explain to you how all this mistaken idea</h2>
  <div class="post-image" role="img" aria-label="Team collaborating around a table with laptops" style="background:linear-gradient(120deg,#5b6a78,#a9b3ba 45%,#7d6a5a)"></div>
  <p class="excerpt">Class aptent taciti sociosqu ad litora torquent per conubia nostra, per inceptos himenaeos. Mauris in erat justo. Nullam ac urna eu felis dapibus condimentum sit amet a augue. Sed non neque elit. Sed ut imperdiet nisi. Proin condimentum fermentum nunc. Etiam pharetra, erat sed fermentum feugiat, velit mauris egestas quam, ut aliquam massa nisl quis neque. Suspendisse in orci enim.</p>
  <span class="continue">CONTINUE READING</span>
</article>

<article class="post" style="top:1170px">
  <div class="meta"><span><i></i>By <b>Daniel Reyes</b></span><span><i></i>28 March 2017</span><span><i></i>Email Automation</span></div>
  <h2 class="post-title">The standard Lorem Ipsum passage used since the awesome as well as explain to you how all this mistaken idea</h2>
  <div class="post-image" role="img" aria-label="Hands typing on a laptop with floating email envelope graphics" style="background:linear-gradient(120deg,#2c3848,#6c7d92 50%,#b5a79a)"></div>
  <p class="excerpt">Class aptent taciti sociosqu ad litora torquent per conubia nostra, per inceptos himenaeos. Mauris in erat justo. Nullam ac urna eu felis dapibus condimentum sit amet a augue. Sed non neque elit. Sed ut imperdiet nisi. Proin condimentum fermentum nunc. Etiam pharetra, erat sed fermentum feugiat, velit mauris egestas quam, ut aliquam massa nisl quis neque. Suspendisse in orci enim.</p>
  <span class="continue">CONTINUE READING</span>
</article>

<article class="post" style="top:1740px">
  <div class="meta"><span><i></i>By <b>Daniel Reyes</b></span><span><i></i>28 March 2017</span><span><i></i>Traveling</span></div>
  <h2 class="post-title">The standard Lorem Ipsum passage used since the awesome as well as explain to you how all this mistaken idea</h2>
  <div class="post-image" role="img" aria-label="Hiker with a backpack overlooking a mountain valley" style="background:linear-gradient(180deg,#9fb7c9 0%,#c9d3d8 35%,#8a7356 65%,#4e4331 100%)"></div>
  <p class="excerpt">Class aptent taciti sociosqu ad litora torquent per conubia nostra, per inceptos himenaeos. Mauris in erat justo. Nullam ac urna eu felis dapibus condimentum sit amet a augue. Sed non neque elit. Sed ut imperdiet nisi. Proin condimentum fermentum nunc. Etiam pharetra, erat sed fermentum feugiat, velit mauris egestas quam, ut aliquam massa nisl quis neque. Suspendisse in orci enim.</p>
  <span class="continue">CONTINUE READING</span>
</article>

<article class="post" style="top:2310px">
  <div class="meta"><span><i></i>By <b>Daniel Reyes</b></span><span><i></i>28 March 2017</span><span><i></i>Rock Climbing</span></div>
  <h2 class="post-title">The standard Lorem Ipsum passage used since the awesome as well as explain to you how all this mistaken idea</h2>
  <div class="post-image" role="img" aria-label="Climber hanging from a rock overhang above a desert landscape" style="background:linear-gradient(180deg,#5f8fc4 0%,#a9c4de 45%,#b59a7a 70%,#6e5a45 100%)"></div>
  <p class="excerpt">Class aptent taciti sociosqu ad litora torquent per conubia nostra, per inceptos himenaeos. Mauris in erat justo. Nullam ac urna eu felis dapibus condimentum sit amet a augue. Sed non neque elit. Sed ut imperdiet nisi. Proin condimentum fermentum nunc. Etiam pharetra, erat sed fermentum feugiat, velit mauris egestas quam, ut aliquam massa nisl quis neque. Suspendisse in orci enim.</p>
  <span class="continue">CONTINUE READING</span>
</article>

<div class="pager"><span>&laquo;Prev</span><span class="current">01</span><span>02</span><span>03</span><span>04</span><span>Next&raquo;</span></div>

<aside>
  <section class="widget about" style="top:608px;height:190px">
    <h3>About Us</h3>
    <p>Class aptent taciti sociosqu ad litora torquent per conubia nostra, per inceptos himenaeos. Mauris in erat justo. Nullam ac urna eu felis dapibus condimentum sit amet a augue. Sed non neque elit sed ut imperdiet.</p>
  </section>

  <section class="widget recent" style="top:820px;height:410px">
    <h3 class="teal">Recent Posts</h3>
    <ul>
      <li><strong>The standard Lorem Ipsum passage used since the awesome</strong><small>By <b>Daniel Reyes</b> · 28 March 2017</small></li>
      <li><strong>The standard Lorem Ipsum passage used since the awesome</strong><small>By <b>Daniel Reyes</b> · 28 March 2017</small></li>
      <li><strong>The standard Lorem Ipsum passage used since the awesome</strong><small>By <b>Daniel Reyes</b> · 28 March 2017</small></li>
      <li><strong>The standard Lorem Ipsum passage used since the awesome</strong><small>By <b>Daniel Reyes</b> · 28 March 2017</small></li>
    </ul>
  </section>

  <section class="widget subscribe" style="top:1252px;height:184px">
    <h3>Subscribe</h3>
    <div class="field">Email Address</div>
    <div class="btn">SUBSCRIBE</div>
  </section>

  <section class="widget archives" style="top:1458px;height:200px">
    <h3 class="teal">Archives</h3>
    <ul><li>January 2017</li><li>February 2017</li><li>March 2017</li><li>April 2017</li><li>May 2017</li></ul>
  </section>

  <section class="widget" style="top:1696px;height:112px">
    <h3 class="dark">Social</h3>
    <div class="side-social"><div class="dot"></div><div class="dot"></div><div class="dot o"></div><div class="dot o"></div><div class="dot"></div></div>
  </section>
</aside>

<footer class="footer">
  <nav><span>About Us</span><span>Contact</span><span>Site Map</span><span>Privacy Policy</span><span>Terms &amp; Conditions</span><span>Accessibility</span></nav>
  <small>© 2017 Bright Pathway</small>
  <div class="to-top"><svg width="32" height="32" viewBox="0 0 32 32"><path d="M10 19 L16 13 L22 19" stroke="#fff" stroke-width="2" fill="none"/></svg></div>
</footer>

</div>
</body>
</html>
```